Jo & Mira's Homepage Design - Florists

Hello PixelHive,

We’re Jo and Mira and we own a lovely flower shop in Marlow. We’re looking to launch a website that gives our customers all information they need to know about getting in contact with us. In time we hope the website will grow and we will want to add new pages as we go along including ecommerce functionality, so the design will need to allow for this.

The brief:
We are looking for 1 homepage design. We have already had our logo designed, which we’ve attached for you to use. At the moment we’re keen to have a homepage design that showcases six of our most popular bouquets, see attached pictures and our contact details. We are looking for a contemporary design that’s inline with our logo. Please do not use dark background colours, we want a clean, light and simple design that looks fresh, modern and professional. Please remember that the majority of web monitors now use a screen resolution of 1366x768. Therefore please do not design a 800 x 600 homepage.

1. Our logo and icon (See attachments)
2. Potential hero images attached for inspiration. 6 Bouquets attached but dont make it look like a bog standard ecommerce site. You dont have to use the 6 bouquets. Our site is more brand as we dont have ecom functionality yet.
3. Our contact details including:

Name:
Jo and Mira’s (note 1 ‘L’ in Mira’s name, use the logo)

Navigation

Homepage needs to include the following copy
‘Free delivery with all orders”
‘Fresh – 7 days of flower freshness guaranteed’
‘Hand delivered and hand prepared by a professional florist’
Very clear call to action to ‘Order today: 0203 554 2071 or email us (visually a clickable link) today

Payment visuals: show that we accept PAYRO/Cardwell/Northern Swift/Quikpay, with logos

Telephone numbers:
0203 554 2071 (Central London)
0208 417 2359 (Greater London)
01628 570213 (Marlow)
07845 190627 (Mobile)

E-mail address
orders@joandmiras.co.uk (Orders)
CS@joandmiras.co.uk (Customer Service)

Chatterly page link (use CH logo)
http://www.facebook.com/joandmiras

The National Petal Guild logo
Attached should be displayed on the bottom of the homepage somewhere, prefer bottom right.

Other sites we like:
http://www.bloomsbyharriet.com
http://maisondepetale.com
Like the fun of this one - http://www.grandpagoose.co.uk/goto/home

Our logo should be a good guide for how we’d like the overall page to look, please use this as a starter for your designs. Fee; free to submit your designs and I’ll feedback on changes.

We look forward to seeing your designs!

Jo & Mira

Industry/Entity Type

Florist

Requirements
Must have
• Please see the attached brief. Please use our logo and icon in the design.
Should not have
• Do not use dark background colours, it should feel light and fresh.

```html
<!DOCTYPE html>
<html lang="en">
<head>
<meta charset="utf-8">
<title>Jo &amp; Mira's Flower Shop</title>
<link href="https://fonts.googleapis.com/css2?family=Arimo:wght@400;700&family=Dancing+Script:wght@600;700&family=Lora:ital,wght@0,400;0,700;1,400;1,700&display=swap" rel="stylesheet">
<style>
:root{
  --red:#e0484f;
  --red-dark:#c8323a;
  --red-light:#ef6b6e;
  --purple:#7b1f74;
  --purple-light:#a24a9a;
  --plum:#8a2c82;
  --text:#333;
  --pink-soft:#f3c9f0;
  --white:#fff;
  --border:#dcdcdc;
}
*{box-sizing:border-box;margin:0;padding:0}
html,body{width:1024px;height:1200px;overflow:hidden;background:var(--white)}
body{position:relative;font-family:Arimo,Arial,sans-serif;color:var(--text)}
.abs{position:absolute}
.floral{position:absolute;border-radius:50%;background:radial-gradient(circle,rgba(220,140,225,.55),rgba(243,201,240,.25) 55%,rgba(255,255,255,0) 72%)}
.serif{font-family:Lora,Georgia,serif}
.logo{left:154px;top:20px;display:flex;align-items:center;gap:10px;font-family:Lora,Georgia,serif;font-weight:700;font-size:44px;color:#3a3a3a}
.logo .dot{width:22px;height:22px;border-radius:50%;background:var(--red)}
.account{right:158px;top:8px;text-align:right;font-size:11px;color:var(--red-dark);line-height:20px}
.account u{color:var(--red-dark)}
.cart{left:708px;top:44px;display:flex;align-items:center;gap:8px;font-family:Lora,Georgia,serif;font-weight:700;font-size:14px;color:#111}
.nav{left:150px;top:95px;width:716px;height:32px;border-radius:6px;background:linear-gradient(#ee6a6c,#d73d45);display:flex;justify-content:space-around;align-items:center;box-shadow:0 1px 2px rgba(0,0,0,.2)}
.nav a{font-family:Lora,Georgia,serif;font-style:italic;font-weight:700;font-size:13.5px;color:var(--white);text-decoration:none;display:flex;align-items:center;gap:5px}
.nav a:first-child{color:#ffe9a6}
.welcome{left:156px;top:140px;font-family:"Dancing Script",cursive;font-weight:700;font-size:22px;color:var(--purple)}
.benefits{left:156px;top:174px;width:290px;list-style:none;font-family:Lora,Georgia,serif;font-style:italic;font-size:14px;color:#222;line-height:16px}
.benefits li{display:flex;gap:10px;margin-bottom:11px}
.benefits svg{flex:none;margin-top:1px}
.order-today{left:160px;top:272px;width:280px;text-align:center;font-family:"Dancing Script",cursive;font-weight:700;font-size:32px;color:var(--plum)}
.phone-btn{left:187px;top:319px;width:228px;height:34px;border-radius:5px;background:linear-gradient(#ee6a6c,#d73d45);color:var(--white);font-size:25px;text-align:center;line-height:34px;letter-spacing:.5px}
.or{left:160px;top:352px;width:280px;text-align:center;font-family:"Dancing Script",cursive;font-weight:700;font-size:28px;color:#555}
.email{left:160px;top:388px;width:280px;text-align:center;font-size:14px;color:#444}
.email a{color:var(--red-dark);text-decoration:underline}
.hero{left:472px;top:140px;width:388px;height:275px;border:4px solid var(--white);border-radius:6px;box-shadow:0 0 4px rgba(0,0,0,.35);background:linear-gradient(160deg,#4d5a3a 0%,#8a7a62 35%,#c9b7a0 55%,#8b6242 80%,#5c3a22 100%);overflow:hidden}
.hero .caption{position:absolute;right:12px;bottom:10px;text-align:right;font-family:Lora,Georgia,serif;color:var(--white);text-shadow:1px 1px 3px #000}
.hero .caption b{display:block;font-size:33px;font-weight:400}
.hero .caption span{font-size:28px;font-weight:700;color:#fff}
.panel-head{height:31px;border-radius:6px 6px 0 0;background:linear-gradient(#a24a9a,#6a1662);color:var(--white);font-family:Lora,Georgia,serif;font-style:italic;font-weight:700;font-size:16px;line-height:31px;padding-left:8px}
.side{left:155px;width:176px}
.links{list-style:none;margin-top:14px;margin-left:10px}
.links li{display:flex;align-items:center;gap:10px;font-family:Lora,Georgia,serif;font-style:italic;font-size:12px;color:#222;height:27px}
.quote{left:158px;top:675px;width:172px;font-family:Lora,Georgia,serif;font-style:italic;font-size:12px;line-height:18px;color:#444}
.quote .mark{position:absolute;left:2px;top:-6px;font-size:44px;line-height:40px;color:var(--red-dark);font-style:normal}
.quote p{text-indent:32px}
.author{left:163px;top:802px;font-family:Lora,Georgia,serif;font-style:italic;font-size:11px;color:#555}
.author b{color:var(--red-dark);font-size:12px}
.btn{background:linear-gradient(#ee6a6c,#d73d45);color:var(--white);font-family:Lora,Georgia,serif;font-weight:700;border-radius:6px;text-align:center;box-shadow:0 1px 2px rgba(0,0,0,.3)}
.read-more{left:254px;top:823px;width:76px;height:25px;line-height:25px;font-size:13px}
.paybox{left:170px;top:906px;width:142px;height:48px;display:flex;align-items:center;gap:8px}
.paybox .sq{width:20px;height:26px;border-radius:3px;background:#c9a94a}
.paybox .name{font-family:Lora,Georgia,serif;font-weight:700;font-size:22px;color:#1d3e7a}
.cards{left:172px;top:957px;display:flex;gap:3px}
.cards span{width:33px;height:20px;border:1px solid var(--border);border-radius:2px;font-size:6.5px;font-weight:700;color:#333;display:flex;align-items:center;justify-content:center;background:#f6f6f6}
.products-head{left:354px;top:427px;width:505px}
.product{position:absolute;width:160px;text-align:center}
.product .photo{width:138px;height:154px;margin:0 auto;border:3px solid var(--white);box-shadow:0 0 4px rgba(0,0,0,.35)}
.product h3{font-family:Lora,Georgia,serif;font-style:italic;font-weight:700;font-size:13px;color:var(--purple);margin-top:14px;line-height:16px}
.product p{font-size:9px;line-height:11.5px;color:#333;margin:5px 12px 0}
.product .buy{display:flex;justify-content:space-between;align-items:center;margin:10px 6px 0 8px}
.product .price{font-family:Lora,Georgia,serif;font-weight:700;font-size:16px;color:var(--red-dark)}
.product .order{width:76px;height:25px;line-height:25px;font-size:13px}
.footer{left:156px;top:1014px;width:698px;height:133px;border-radius:0 0 8px 8px;background:linear-gradient(#e65a5e,#cf3d44);color:var(--white);font-size:9.5px}
.footer .col{position:absolute;top:0;height:100%}
.footer .divider{position:absolute;top:0;width:1px;height:100%;background:rgba(255,255,255,.25)}
.footer h4{font-size:13px;font-weight:700;margin:12px 0 10px}
.footer ul{list-style:none;line-height:19px;margin-top:10px}
.footer .lines{line-height:11.5px}
.social{display:flex;align-items:center;gap:5px;font-size:11px;font-weight:700;margin-top:2px}
.social .sq{width:18px;height:18px;background:#2f5aa3;border-radius:3px}
.badge{width:58px;height:30px;border-radius:4px;background:#f0b24a;margin-top:16px}
</style>
</head>
<body>

<div class="floral" style="left:-30px;top:-20px;width:180px;height:160px" role="img" aria-label="Pink floral decoration"></div>
<div class="floral" style="left:620px;top:-60px;width:300px;height:220px" role="img" aria-label="Pink floral decoration"></div>
<div class="floral" style="left:860px;top:100px;width:200px;height:240px" role="img" aria-label="Pink floral decoration"></div>
<div class="floral" style="left:880px;top:420px;width:180px;height:220px" role="img" aria-label="Pink floral decoration"></div>
<div class="floral" style="left:-40px;top:780px;width:200px;height:260px" role="img" aria-label="Pink floral decoration"></div>
<div class="floral" style="left:870px;top:960px;width:200px;height:260px" role="img" aria-label="Pink floral decoration"></div>
<div class="floral" style="left:150px;top:1140px;width:700px;height:120px" role="img" aria-label="Pink floral decoration"></div>

<header>
  <div class="abs logo"><span class="dot"></span>Jo &amp; Mira's</div>
  <div class="abs account">YOUR ACCOUNT<br>Welcome, ( <u>log in</u> )</div>
  <div class="abs cart">
    <svg width="34" height="30" viewBox="0 0 34 30"><path d="M2 4h6l4 16h16l4-12H10" fill="none" stroke="#b88a00" stroke-width="2"/><path d="M10 8h22l-4 12H12z" fill="#f3c515"/><circle cx="14" cy="25" r="2.5" fill="#806000"/><circle cx="26" cy="25" r="2.5" fill="#806000"/></svg>
    My Cart : 0 Item (s)
  </div>
  <nav class="abs nav">
    <a>✽ Classic Flowers</a><a>✽ Luxury Bouquets</a><a>✽ Platinum Collection</a><a>✽ Autumn Flowers</a><a>✽ Luxury Roses</a>
  </nav>
</header>

<section class="intro">
  <h1 class="abs welcome">Welcome to Jo and Mira's Flower Shop</h1>
  <ul class="abs benefits">
    <li><svg width="12" height="12" viewBox="0 0 12 12"><g stroke="#e0484f" stroke-width="2.4" stroke-linecap="round"><path d="M6 1v10M1 6h10M2.5 2.5l7 7M9.5 2.5l-7 7"/></g></svg>Free delivery with all orders</li>
    <li><svg width="12" height="12" viewBox="0 0 12 12"><g stroke="#e0484f" stroke-width="2.4" stroke-linecap="round"><path d="M6 1v10M1 6h10M2.5 2.5l7 7M9.5 2.5l-7 7"/></g></svg>Fresh 7 days of flower freshness guaranteed</li>
    <li><svg width="12" height="12" viewBox="0 0 12 12"><g stroke="#e0484f" stroke-width="2.4" stroke-linecap="round"><path d="M6 1v10M1 6h10M2.5 2.5l7 7M9.5 2.5l-7 7"/></g></svg>Hand delivered and hand prepared by a professional florist</li>
  </ul>
  <div class="abs order-today">Order Today</div>
  <div class="abs phone-btn">0203 554 2071</div>
  <div class="abs or">or</div>
  <div class="abs email">Email us : <a>orders@joandmiras.co.uk</a></div>
  <div class="abs hero" role="img" aria-label="Autumn bouquet of calla lilies and roses wrapped in hessian on a wooden table">
    <div class="caption"><b>Autumn Love</b><span>£24.99</span></div>
  </div>
</section>

<aside>
  <div class="abs side" style="top:427px">
    <div class="panel-head">Usefull Links</div>
    <ul class="links">
      <li><svg width="12" height="12" viewBox="0 0 12 12"><g stroke="#e0484f" stroke-width="2.4" stroke-linecap="round"><path d="M6 1v10M1 6h10M2.5 2.5l7 7M9.5 2.5l-7 7"/></g></svg>Latest Designs</li>
      <li><svg width="12" height="12" viewBox="0 0 12 12"><g stroke="#e0484f" stroke-width="2.4" stroke-linecap="round"><path d="M6 1v10M1 6h10M2.5 2.5l7 7M9.5 2.5l-7 7"/></g></svg>Our Favourites</li>
      <li><svg width="12" height="12" viewBox="0 0 12 12"><g stroke="#e0484f" stroke-width="2.4" stroke-linecap="round"><path d="M6 1v10M1 6h10M2.5 2.5l7 7M9.5 2.5l-7 7"/></g></svg>Delivery Information</li>
      <li><svg width="12" height="12" viewBox="0 0 12 12"><g stroke="#e0484f" stroke-width="2.4" stroke-linecap="round"><path d="M6 1v10M1 6h10M2.5 2.5l7 7M9.5 2.5l-7 7"/></g></svg>Customer Service</li>
      <li><svg width="12" height="12" viewBox="0 0 12 12"><g stroke="#e0484f" stroke-width="2.4" stroke-linecap="round"><path d="M6 1v10M1 6h10M2.5 2.5l7 7M9.5 2.5l-7 7"/></g></svg>FAQ</li>
      <li><svg width="12" height="12" viewBox="0 0 12 12"><g stroke="#e0484f" stroke-width="2.4" stroke-linecap="round"><path d="M6 1v10M1 6h10M2.5 2.5l7 7M9.5 2.5l-7 7"/></g></svg>About Us</li>
    </ul>
  </div>
  <div class="abs side" style="top:638px"><div class="panel-head">Client Testimonials</div></div>
  <div class="abs quote"><span class="mark">“</span><p>Lorem Ipsum is simply dummy text of the printing and typesetting industry. Lorem Ipsum has been the industry's standard dummytext ever since the 1500s, when an unknown printer took a galley of type ....</p></div>
  <div class="abs author"><b>Sam</b> 15thr sept '12</div>
  <div class="abs btn read-more">Read More</div>
  <div class="abs side" style="top:863px"><div class="panel-head">Payment Visuals</div></div>
  <div class="abs paybox"><span class="sq"></span><span class="name">Quikpay</span></div>
  <div class="abs cards"><span>PAYRO</span><span>Cardwell</span><span>Roamcard</span><span>N. Swift</span></div>
</aside>

<main>
  <div class="abs products-head panel-head">Our Products</div>

  <div class="product" style="left:351px;top:468px">
    <div class="photo" role="img" aria-label="Lilac rose arrangement in a vintage frame" style="background:linear-gradient(160deg,#8d8a80,#b7a8c4 45%,#6f7f5a 80%,#4a4a42)"></div>
    <h3>Autumn Wonders</h3><p>Lorem Ipsum is simply dummy text of the printing and typesetting industry.</p>
    <div class="buy"><span class="price">£27.99</span><span class="btn order">Order Now</span></div>
  </div>
  <div class="product" style="left:528px;top:468px">
    <div class="photo" role="img" aria-label="Heart shaped wreath of green and pink flowers" style="background:linear-gradient(160deg,#e8e8e2,#8c9a6a 40%,#c58e8e 65%,#eeeeea)"></div>
    <h3>Be My Sweet Heart</h3><p>Lorem Ipsum is simply dummy text of the printing and typesetting industry.</p>
    <div class="buy"><span class="price">£35.99</span><span class="btn order">Order Now</span></div>
  </div>
  <div class="product" style="left:704px;top:468px">
    <div class="photo" role="img" aria-label="Bouquet of red and orange roses" style="background:linear-gradient(160deg,#fbe9e4,#e2401e 35%,#c5200f 70%,#f3d9cf)"></div>
    <h3>Roses are Red</h3><p>Lorem Ipsum is simply dummy text of the printing and typesetting industry.</p>
    <div class="buy"><span class="price">£49.99</span><span class="btn order">Order Now</span></div>
  </div>

  <div class="product" style="left:351px;top:740px">
    <div class="photo" role="img" aria-label="Bright pink and peach hand tied bouquet" style="background:linear-gradient(160deg,#8a6a52,#e8487c 35%,#f08a66 60%,#7a5a44)"></div>
    <h3>We are Young,<br>We are Free</h3><p>Lorem Ipsum is simply dummy text of the printing.</p>
    <div class="buy"><span class="price">£19.99</span><span class="btn order">Order Now</span></div>
  </div>
  <div class="product" style="left:528px;top:740px">
    <div class="photo" role="img" aria-label="Soft pink and white wedding flowers" style="background:linear-gradient(160deg,#6e8a5c,#f1d8d4 40%,#e6c4c0 65%,#5d6e4c)"></div>
    <h3>Wedding Flowers</h3><p>Lorem Ipsum is simply dummy text of the printing and typesetting industry.</p>
    <div class="buy"><span class="price">£35.99</span><span class="btn order">Order Now</span></div>
  </div>
  <div class="product" style="left:704px;top:740px">
    <div class="photo" role="img" aria-label="Autumn bouquet wrapped in hessian" style="background:linear-gradient(160deg,#4d5a3a,#c9b7a0 45%,#8b6242 75%,#5c3a22)"></div>
    <h3>Autumn Love</h3><p>Lorem Ipsum is simply dummy text of the printing and typesetting industry.</p>
    <div class="buy"><span class="price">£24.99</span><span class="btn order">Order Now</span></div>
  </div>
</main>

<footer class="abs footer">
  <div class="col" style="left:20px">
    <ul><li><u>About Us</u></li><li>Customer Service</li><li>Site Map</li><li>Search Terms</li><li>Advanced Search</li><li>Contact Us</li></ul>
  </div>
  <span class="divider" style="left:132px"></span>
  <div class="col" style="left:162px">
    <h4>Telephone numbers :</h4>
    <div class="lines">0203 554 2071 (Central London)<br>0208 417 2359 (Greater London)<br>01628 570213 (Marlow)<br>07845 190627 (Mobile)</div>
  </div>
  <span class="divider" style="left:330px"></span>
  <div class="col" style="left:367px">
    <h4>E-mail address</h4>
    <div class="lines">orders@joandmiras.co.uk &nbsp;(Orders)<br>CS@joandmiras.co.uk (Customer Service)</div>
  </div>
  <span class="divider" style="left:576px"></span>
  <div class="col" style="left:614px;width:80px">
    <h4>Find us on</h4>
    <div class="social"><span class="sq"></span>Chatterly</div>
    <div class="badge" role="img" aria-label="The National Petal Guild member badge"></div>
  </div>
</footer>

</body>
</html>
```